Business Card Design Project

I require a business card with the following information on them for various different people;
name
m:
f:
e:
I have a logo already and will attached that. We are in the construction industry. I require something clean and simple but eye catching at the same time. You can use another colour with our logo if you like and you can style the logo as well if you wish. I am open.
Also it needs to be front and back design.
Industry/Entity Type
Construction
Requirements
Must have
- Logo, name, mobile, fax and email address.
Front and back design

```html
<!DOCTYPE html>
<html lang="en">
<head>
<meta charset="utf-8">
<title>Stonebrook Developments – Business Card</title>
<link rel="stylesheet" href="https://fonts.googleapis.com/css2?family=Open+Sans:wght@300;400;600;700&display=swap">
<style>
  :root {
    --page-bg: #ffffff;
    --card-bg: #ffffff;
    --card-edge: #cfcfcf;
    --ink: #111111;
    --brand-grey: #3d3d3f;
    --brand-green: #5fd40e;
    --accent-green: #63dd0f;
  }
  * { margin: 0; padding: 0; box-sizing: border-box; }
  html, body {
    width: 964px;
    height: 1200px;
    overflow: hidden;
    background: var(--page-bg);
    font-family: "Open Sans", Arial, sans-serif;
    color: var(--ink);
  }
  .sheet { position: relative; width: 964px; height: 1200px; }
  .card {
    position: absolute;
    left: 21px;
    width: 922px;
    height: 555px;
    background: var(--card-bg);
    border: 1px solid var(--card-edge);
    overflow: hidden;
  }
  .card--front { top: 21px; }
  .card--back { top: 611px; }
  .card__corner { position: absolute; left: 0; top: 0; width: 100%; height: 100%; }

  .brand-name {
    position: absolute;
    left: 16px;
    top: 8px;
    font-weight: 300;
    color: var(--brand-grey);
    line-height: 1;
  }
  .brand-name__main { display: block; font-size: 128px; letter-spacing: -3px; }
  .brand-name__sub { display: block; font-size: 50px; letter-spacing: 26px; margin-top: 4px; padding-left: 10px; }

  .contact-person {
    position: absolute;
    left: 32px;
    top: 420px;
  }
  .contact-person__name { font-size: 38px; font-weight: 600; line-height: 1.15; }
  .contact-person__email { font-size: 27px; font-weight: 400; line-height: 1.3; }

  .contact-lines {
    position: absolute;
    right: 50px;
    top: 432px;
    text-align: right;
    font-size: 28px;
    line-height: 1.35;
  }

  .back-mark {
    position: absolute;
    left: 0;
    top: 0;
    width: 100%;
    height: 100%;
    display: flex;
    align-items: center;
    justify-content: center;
    gap: 22px;
  }
  .back-mark__square { width: 46px; height: 46px; background: var(--brand-green); border-radius: 6px; }
  .back-mark__name { font-size: 70px; font-weight: 300; color: var(--brand-green); letter-spacing: -1px; }
</style>
</head>
<body>
<main class="sheet">
  <section class="card card--front" aria-label="Business card front">
    <h1 class="brand-name">
      <span class="brand-name__main">Stonebrook</span>
      <span class="brand-name__sub">DEVELOPMENTS</span>
    </h1>
    <div class="contact-person">
      <p class="contact-person__name">Daniel Hartley</p>
      <p class="contact-person__email">d.hartley@stonebrookbuild.com</p>
    </div>
    <div class="contact-lines">
      <p>Mobile: 555 010 482</p>
      <p>Fax: 555 010 483</p>
    </div>
    <svg class="card__corner" viewBox="0 0 922 555" aria-hidden="true">
      <polygon points="864,555 922,555 922,520" fill="var(--accent-green)"/>
    </svg>
  </section>

  <section class="card card--back" aria-label="Business card back">
    <div class="back-mark">
      <span class="back-mark__square"></span>
      <span class="back-mark__name">Stonebrook</span>
    </div>
    <svg class="card__corner" viewBox="0 0 922 555" aria-hidden="true">
      <polygon points="0,520 0,555 58,555" fill="var(--accent-green)"/>
    </svg>
  </section>
</main>
</body>
</html>
```